Skyreach Northern Flights
Private Charters
Skyreach Northern Flights  - Aviation
Creative Brief
Cutting-Edge
Tamara Holbrook
Business Development
5127 N. Darrow, Suite 240 Scottsdale, AZ 85254
tholbrook@skyreachnorthernflights.example
www.skyreachnorthernflights.example

```html
<!DOCTYPE html>
<html lang="en">
<head>
<meta charset="utf-8">
<title>Skyreach Northern Flights — Stationery Set</title>
<link rel="stylesheet" href="https://fonts.googleapis.com/css2?family=Cinzel:wght@500&family=Open+Sans:wght@400;600&display=swap">
<style>
  :root {
    --paper: #ffffff;
    --canvas: #ffffff;
    --slate: #6c6c6f;
    --slate-light: #86868a;
    --slate-dark: #55555a;
    --maroon: #7a1f24;
    --ink: #3a3a3c;
    --muted: #9a9a9e;
    --edge: #dcdcdc;
  }
  * { box-sizing: border-box; margin: 0; padding: 0; }
  html, body { width: 1200px; height: 720px; overflow: hidden; background: var(--canvas); }
  body { position: relative; font-family: "Open Sans", Arial, sans-serif; color: var(--ink); }

  .piece { position: absolute; box-shadow: 0 1px 3px rgba(0,0,0,.18); }
  .sheet { background: var(--paper); }
  .slate { background: radial-gradient(ellipse at 50% 40%, var(--slate-light), var(--slate) 60%, var(--slate-dark)); }

  .label { position: absolute; font-size: 7px; color: var(--muted); letter-spacing: .5px; }

  .wordmark {
    position: absolute; font-family: "Cinzel", Georgia, serif; font-weight: 500;
    text-align: center; line-height: 1.1; color: var(--slate-dark); letter-spacing: .5px;
  }
  .wordmark.on-slate { color: #ffffff; }
  .wordmark .dot { display: block; margin: 0 auto 3px; width: 8px; height: 8px; background: currentColor; }
  .wordmark .tagline { font-size: .5em; letter-spacing: 2px; margin-top: 3px; }

  .small-text { position: absolute; font-size: 4.5px; line-height: 1.5; color: var(--ink); white-space: nowrap; }
  .maroon-band { position: absolute; left: 0; right: 0; height: 4px; background: var(--maroon); }

  .envelope-flap { position: absolute; left: 0; top: 0; }

  .folder-pocket {
    position: absolute; left: 0; bottom: 0; width: 292px; height: 150px;
    background: linear-gradient(180deg, var(--slate-dark), var(--slate));
    border-top: 1px solid rgba(255,255,255,.25);
  }
  .card-slot { position: absolute; left: 78px; top: 28px; width: 84px; height: 50px; background: var(--paper); }

  .cd-disc { position: absolute; }

  .compliments-title { position: absolute; font-size: 9px; color: var(--ink); letter-spacing: .5px; }
</style>
</head>
<body>

  <!-- Business card -->
  <span class="label" style="left:60px; top:46px;">Front</span>
  <span class="label" style="left:150px; top:46px;">Back</span>
  <section class="piece sheet business-card-front" style="left:29px; top:58px; width:80px; height:48px;">
    <div class="small-text" style="left:6px; top:6px; font-size:4px;">
      <strong>Tamara Holbrook</strong><br>Business Development
    </div>
    <div class="small-text" style="left:6px; top:24px; font-size:3px;">
      5127 N. Darrow, Suite 240 Harlow Springs, CO 80999<br>
      T 719 555 0142<br>
      tholbrook@skyreachnorthernflights.example<br>
      www.skyreachnorthernflights.example
    </div>
    <div class="maroon-band" style="bottom:0; height:2px;"></div>
  </section>
  <section class="piece slate business-card-back" style="left:118px; top:58px; width:80px; height:48px;">
    <div class="wordmark on-slate" style="left:4px; right:4px; top:13px; font-size:5.5px;">
      <span class="dot" style="width:5px;height:5px;margin-bottom:2px;"></span>Skyreach Northern Flights
    </div>
  </section>

  <!-- Envelope -->
  <span class="label" style="left:60px; top:130px;">Envelope</span>
  <section class="piece sheet envelope-front" style="left:12px; top:142px; width:245px; height:120px;">
    <div class="wordmark" style="left:10px; top:10px; width:70px; font-size:6px;">
      <span class="dot" style="width:5px;height:5px;"></span>Skyreach Northern Flights
    </div>
    <div class="small-text" style="left:12px; top:85px; font-size:3.6px;">
      5127 N. Darrow, Suite 240<br>Harlow Springs, CO 80999
    </div>
  </section>
  <section class="piece sheet envelope-back" style="left:12px; top:275px; width:245px; height:125px;">
    <svg class="envelope-flap" width="245" height="70" viewBox="0 0 245 70" aria-hidden="true">
      <path d="M0 0 H245 V10 L132 66 Q122.5 71 113 66 L0 10 Z" fill="var(--slate)"/>
    </svg>
    <div class="wordmark on-slate" style="left:0; right:0; top:18px; font-size:5.5px;">
      <span class="dot" style="width:5px;height:5px;"></span>Skyreach Northern Flights
    </div>
  </section>

  <!-- Letterhead -->
  <span class="label" style="left:410px; top:30px;">Letterhead</span>
  <section class="piece sheet letterhead" style="left:288px; top:42px; width:282px; height:355px;">
    <div class="wordmark" style="left:0; right:0; top:22px; font-size:8px;">
      <span class="dot" style="width:6px;height:6px;"></span>Skyreach Northern Flights
    </div>
    <div class="small-text" style="left:40px; top:332px; font-size:3.8px;">
      5127 N. Darrow, Suite 240 Harlow Springs, CO 80999 · T 719 555 0142 · F 719 555 0143
    </div>
    <div class="maroon-band" style="bottom:0; height:4px;"></div>
  </section>

  <!-- Presentation folder -->
  <span class="label" style="left:860px; top:8px;">Presentation Folder</span>
  <section class="piece presentation-folder" style="left:620px; top:20px; width:575px; height:500px;">
    <div class="slate" style="position:absolute; left:0; top:0; width:292px; height:500px;">
      <div class="wordmark on-slate" style="left:0; right:0; top:305px; font-size:6px;">
        <span class="dot" style="width:5px;height:5px;"></span>Skyreach Northern Flights
      </div>
      <div class="small-text" style="left:0; right:0; top:332px; text-align:center; color:#e6e6e6; font-size:3.6px;">
        5127 N. Darrow, Suite 240 Harlow Springs, CO 80999<br>www.skyreachnorthernflights.example
      </div>
      <div class="folder-pocket">
        <div class="card-slot">
          <div class="small-text" style="left:5px; top:6px; font-size:3.4px;"><strong>Tamara Holbrook</strong><br>Business Development</div>
          <div class="maroon-band" style="bottom:0; height:2px;"></div>
        </div>
      </div>
    </div>
    <div class="sheet" style="position:absolute; left:292px; top:0; width:283px; height:500px;">
      <div class="wordmark" style="left:20px; right:20px; top:50px; font-size:17px; color:var(--ink);">
        <span class="dot" style="width:12px;height:12px;margin-bottom:6px;color:var(--maroon);"></span>Skyreach Northern Flights
        <div style="font-size:8px; letter-spacing:3px; margin-top:4px;">Private Charters</div>
      </div>
    </div>
  </section>

  <!-- Compliment slip -->
  <span class="label" style="left:14px; top:433px;">Compliment Slip</span>
  <section class="piece sheet compliment-slip-front" style="left:12px; top:445px; width:200px; height:130px;">
    <div class="wordmark" style="left:10px; top:10px; width:60px; font-size:5px;">
      <span class="dot" style="width:4px;height:4px;"></span>Skyreach Northern Flights
    </div>
    <p class="compliments-title" style="left:12px; top:55px;">With Compliments</p>
    <div class="small-text" style="left:12px; top:95px; font-size:3.4px;">
      5127 N. Darrow, Suite 240 Harlow Springs, CO 80999<br>T 719 555 0142
    </div>
    <div class="maroon-band" style="bottom:0; height:3px;"></div>
  </section>
  <section class="piece slate compliment-slip-back" style="left:228px; top:445px; width:185px; height:130px;">
    <div class="wordmark on-slate" style="left:20px; right:20px; top:40px; font-size:10px;">
      <span class="dot"></span>Skyreach Northern Flights
      <div style="font-size:5px; letter-spacing:2px; margin-top:3px;">Private Charters</div>
    </div>
  </section>

  <!-- CD -->
  <span class="label" style="left:700px; top:574px;">CD Label</span>
  <svg class="cd-disc" style="left:656px; top:586px;" width="128" height="128" viewBox="0 0 128 128" aria-hidden="true">
    <circle cx="64" cy="64" r="62" fill="var(--paper)" stroke="var(--edge)"/>
    <circle cx="64" cy="64" r="13" fill="none" stroke="var(--edge)"/>
    <circle cx="64" cy="64" r="6" fill="var(--canvas)" stroke="var(--edge)"/>
  </svg>
  <div class="wordmark" style="left:672px; top:600px; width:96px; font-size:5px;">
    <span class="dot" style="width:4px;height:4px;"></span>Skyreach Northern Flights
  </div>

  <!-- CD cover -->
  <span class="label" style="left:980px; top:528px;">CD Cover</span>
  <section class="piece cd-cover" style="left:822px; top:540px; width:358px; height:165px;">
    <div class="slate" style="position:absolute; left:0; top:0; width:188px; height:165px;">
      <div class="wordmark on-slate" style="left:0; right:0; top:120px; font-size:5px;">
        <span class="dot" style="width:4px;height:4px;"></span>Skyreach Northern Flights
      </div>
    </div>
    <div class="sheet" style="position:absolute; left:188px; top:0; width:170px; height:165px;">
      <div class="wordmark" style="left:10px; right:10px; top:22px; font-size:9px; color:var(--ink);">
        <span class="dot" style="color:var(--maroon);"></span>Skyreach Northern Flights
        <div style="font-size:4.5px; letter-spacing:2px; margin-top:3px;">Private Charters</div>
      </div>
    </div>
  </section>

</body>
</html>
```